Neighborhood Market Comparables

I am a realtor and am in need of a jumbo postcard 6.25 x 9 template that is 2 sided for "neighborhood farming". I would like to be able to change out neighborhood names, average sales prices, number of Active listings, number of Sold listings, average square footage and price per square foot as well as days on market, and number of leased homes (active, leased and days on market). I'd like the background, images, and my information all set but be able to change the numbers for each category as well as change the month of the report. I would like a generic blurb on the back as I will be mailing these but want the ability to change the verbiage. I've attached a few copies of fliers I have found online as a point of reference. I like the Awe and then Some as a tag line for me as a realtor. Please let me know what else you may need. Thank you.

Target Market(s)

Neighbors interested in the real estate market and identify those looking to buy or sell a home.

Industry/Entity Type

Real Estate Agent

Font styles to use
Sans Serif

Colors
33a6d7
ec1f27
3176b5
0392cd
85abd2

Requirements
Must have
• Ability to change out neighborhood names, average sales prices, number of Active listings, number of Sold listings, average square footage and price per square foot as well as days on market, and number of leased homes (active, leased and days on market). I'd like the background, images, and my information all set but be able to change the numbers for each category as well as change the month of the report. I would like a generic blurb on the back as I will be mailing these but want the ability to change the verbiage. I've attached a few copies of fliers I have found online as a point of reference. I like the Awe and then Some as a tag line for me as a realtor. Please let me know what else you may need. Thank you.
Nice to have
• I have attached several ideas from ones I have found online. Also would be able to compare year after year.

```html
<!DOCTYPE html>
<html lang="en">
<head>
<meta charset="utf-8">
<title>Market Snapshot Postcard</title>
<link rel="stylesheet" href="https://fonts.googleapis.com/css2?family=Archivo+Black&family=Oswald:wght@400;500&family=Roboto+Condensed:wght@700&family=Arimo:wght@400;700&display=swap">
<style>
  :root {
    --brand-red: #c01f2e;
    --stat-red: #c3202f;
    --ink: #000000;
    --paper: #ffffff;
    --muted: #bdbdbd;
    --accent-soft: #e59a8c;
    --page: #ffffff;
    --skyline-dark: #111111;
    --skyline-mid: #5a4b4b;
    --rule: #333333;
  }
  * { box-sizing: border-box; margin: 0; padding: 0; }
  html, body { width: 1200px; height: 843px; overflow: hidden; background: var(--page); }
  .postcard {
    position: absolute; left: 62px; top: 40px; width: 1056px; height: 746px;
    background: var(--paper); border: 2px solid var(--ink); overflow: hidden;
    font-family: "Arimo", Arial, sans-serif;
  }
  .header { position: absolute; left: 0; top: 0; width: 100%; height: 270px; background: var(--brand-red); }
  .title { position: absolute; left: 52px; top: 34px; font-size: 50px; line-height: 1; letter-spacing: 0.5px; white-space: nowrap; }
  .title-strong { font-family: "Archivo Black", "Arial Black", sans-serif; color: var(--ink); font-size: 44px; }
  .title-light { font-family: "Oswald", "Arial Narrow", sans-serif; font-weight: 500; color: var(--paper); }
  .agent { position: absolute; left: 692px; top: 32px; display: flex; align-items: center; gap: 20px; white-space: nowrap; }
  .brokerage { font-family: "Roboto Condensed", "Arial Narrow", sans-serif; font-weight: 700; font-size: 26px; color: var(--accent-soft); }
  .agent-name { font-family: "Roboto Condensed", "Arial Narrow", sans-serif; font-weight: 700; color: var(--paper); font-size: 31px; line-height: 1.05; }
  .agent-role { font-family: "Roboto Condensed", "Arial Narrow", sans-serif; font-weight: 700; color: var(--paper); font-size: 22px; }
  .skyline {
    position: absolute; left: 0; top: 100px; width: 100%; height: 100px;
    background: linear-gradient(to bottom, var(--brand-red) 0%, var(--skyline-mid) 35%, var(--skyline-dark) 100%);
  }
  .area-band {
    position: absolute; left: 0; top: 200px; width: 100%; height: 70px; background: var(--ink);
    display: flex; align-items: center; padding: 0 72px 0 66px; white-space: nowrap;
  }
  .area-name { font-family: "Oswald", "Arial Narrow", sans-serif; font-weight: 400; color: var(--paper); font-size: 48px; line-height: 1; letter-spacing: 1px; }
  .area-region { font-family: "Arimo", Arial, sans-serif; font-weight: 700; color: var(--muted); font-size: 28px; margin-left: 26px; margin-top: 8px; }
  .report-month { font-family: "Arimo", Arial, sans-serif; font-weight: 700; color: var(--muted); font-size: 33px; margin-left: auto; }
  .stat {
    position: absolute; width: 230px; transform: translateX(-50%);
    display: flex; flex-direction: column; align-items: center; text-align: center;
  }
  .stat-label { font-size: 19px; line-height: 1.2; color: var(--ink); display: flex; align-items: flex-end; justify-content: center; }
  .row-top .stat-label { height: 26px; }
  .row-bottom .stat-label { height: 48px; }
  .stat-icon { width: 92px; height: 92px; margin-top: 10px; }
  .stat-value { font-family: "Roboto Condensed", "Arial Narrow", sans-serif; font-weight: 700; color: var(--stat-red); font-size: 33px; line-height: 1; margin-top: 8px; }
  .row-top .stat { top: 286px; }
  .row-bottom .stat { top: 484px; }
  .divider { position: absolute; left: 91px; top: 476px; width: 894px; height: 2px; background: var(--rule); }
  .footer {
    position: absolute; left: 0; bottom: 0; width: 100%; height: 48px; background: var(--ink);
    display: flex; align-items: center; justify-content: center; gap: 22px;
    color: var(--muted); font-weight: 700; font-size: 19px; letter-spacing: 0.5px;
  }
</style>
</head>
<body>
<article class="postcard">
  <header class="header">
    <h1 class="title"><span class="title-strong">MARKET</span> <span class="title-light">SNAPSHOT</span></h1>
    <div class="skyline" role="img" aria-label="City skyline silhouette with lit windows"></div>
    <div class="agent">
      <span class="brokerage">Harbor Realty</span>
      <div>
        <div class="agent-name">Dana Whitfield</div>
        <div class="agent-role">Agent</div>
      </div>
    </div>
    <div class="area-band">
      <span class="area-name">THE BEACH</span>
      <span class="area-region">North Texas</span>
      <span class="report-month">March 2018</span>
    </div>
  </header>

  <section class="stats row-top">
    <div class="stat" style="left:185px">
      <div class="stat-label">Average Sale Price</div>
      <svg class="stat-icon" viewBox="0 0 100 100" fill="none" stroke="#000" stroke-width="8" stroke-linejoin="miter">
        <path d="M8 50 L50 12 L92 50"/><path d="M22 44 V90 H78 V44"/><path d="M70 18 V34"/>
        <text x="50" y="80" font-family="Arial Black, sans-serif" font-weight="900" font-size="38" text-anchor="middle" fill="#000" stroke="none">$</text>
      </svg>
      <div class="stat-value">$359,100</div>
    </div>
    <div class="stat" style="left:431px">
      <div class="stat-label">Active Listings</div>
      <svg class="stat-icon" viewBox="0 0 100 100" fill="none" stroke="#000" stroke-width="8">
        <path d="M6 52 L46 14 L64 30"/><path d="M20 46 V90 H74 V58"/><path d="M38 90 V66 H54 V90"/>
        <circle cx="74" cy="34" r="14"/><path d="M84 44 L96 56"/>
        <path d="M74 27 V41 M67 34 H81" stroke-width="5"/>
      </svg>
      <div class="stat-value">895</div>
    </div>
    <div class="stat" style="left:685px">
      <div class="stat-label">Sold Listings</div>
      <svg class="stat-icon" viewBox="0 0 100 100" fill="none" stroke="#000" stroke-width="7">
        <circle cx="50" cy="14" r="8" fill="#000"/><path d="M50 20 L14 50 M50 20 L86 50" stroke-width="5"/>
        <rect x="6" y="48" width="88" height="44" fill="#000" stroke="none"/>
        <rect x="14" y="56" width="72" height="28" fill="#fff" stroke="none"/>
        <text x="50" y="78" font-family="Arial Black, sans-serif" font-weight="900" font-size="19" text-anchor="middle" fill="#000" stroke="none">SOLD</text>
      </svg>
      <div class="stat-value">75</div>
    </div>
    <div class="stat" style="left:909px">
      <div class="stat-label">Average Sq Ft</div>
      <svg class="stat-icon" viewBox="0 0 100 100" fill="#000">
        <rect x="20" y="4" width="14" height="92"/><rect x="8" y="18" width="12" height="8"/><rect x="8" y="38" width="12" height="8"/>
        <rect x="34" y="18" width="62" height="14"/><rect x="46" y="10" width="5" height="8"/><rect x="62" y="10" width="5" height="8"/><rect x="78" y="10" width="5" height="8"/>
        <text x="66" y="78" font-family="Arial Black, sans-serif" font-weight="900" font-size="34" text-anchor="middle">ft</text>
      </svg>
      <div class="stat-value">3200</div>
    </div>
  </section>

  <div class="divider"></div>

  <section class="stats row-bottom">
    <div class="stat" style="left:185px">
      <div class="stat-label">Price per Sq Ft</div>
      <svg class="stat-icon" viewBox="0 0 100 100" fill="#000">
        <rect x="20" y="4" width="14" height="92"/><rect x="8" y="18" width="12" height="8"/><rect x="8" y="38" width="12" height="8"/>
        <rect x="34" y="18" width="62" height="14"/><rect x="46" y="10" width="5" height="8"/><rect x="62" y="10" width="5" height="8"/><rect x="78" y="10" width="5" height="8"/>
        <text x="66" y="78" font-family="Arial Black, sans-serif" font-weight="900" font-size="34" text-anchor="middle">ft</text>
      </svg>
      <div class="stat-value">$11.25</div>
    </div>
    <div class="stat" style="left:431px">
      <div class="stat-label">Days on<br>the Market</div>
      <svg class="stat-icon" viewBox="0 0 100 100" fill="#000">
        <rect x="6" y="16" width="88" height="80" rx="8"/><rect x="14" y="36" width="72" height="52" fill="#fff"/>
        <rect x="22" y="4" width="10" height="22" rx="4" stroke="#fff" stroke-width="3"/><rect x="68" y="4" width="10" height="22" rx="4" stroke="#fff" stroke-width="3"/>
        <rect x="26" y="54" width="12" height="10"/><rect x="44" y="54" width="12" height="10"/><rect x="62" y="54" width="12" height="10"/>
        <rect x="14" y="70" width="72" height="18"/>
      </svg>
      <div class="stat-value">45</div>
    </div>
    <div class="stat" style="left:685px">
      <div class="stat-label">Pending Sales</div>
      <svg class="stat-icon" viewBox="0 0 100 100">
        <circle cx="50" cy="50" r="47" fill="#000"/>
        <path d="M26 56 A25 25 0 0 1 70 30" fill="none" stroke="#fff" stroke-width="8"/><path d="M62 20 L80 26 L70 42 Z" fill="#fff"/>
        <path d="M74 44 A25 25 0 0 1 30 70" fill="none" stroke="#fff" stroke-width="8"/><path d="M38 80 L20 74 L30 58 Z" fill="#fff"/>
        <text x="50" y="62" font-family="Arial Black, sans-serif" font-weight="900" font-size="32" text-anchor="middle" fill="#fff">$</text>
      </svg>
      <div class="stat-value">110</div>
    </div>
    <div class="stat" style="left:909px">
      <div class="stat-label">Leased Homes</div>
      <svg class="stat-icon" viewBox="0 0 100 100" fill="none" stroke="#000" stroke-width="8">
        <path d="M6 52 L46 14 L60 27"/><path d="M20 46 V90 H74 V58"/><path d="M38 90 V66 H54 V90"/>
        <circle cx="74" cy="34" r="16" fill="#000"/>
        <text x="74" y="43" font-family="Arial Black, sans-serif" font-weight="900" font-size="24" text-anchor="middle" fill="#fff" stroke="none">#</text>
      </svg>
      <div class="stat-value">55</div>
    </div>
  </section>

  <footer class="footer">
    <span class="contact-phone">Phone Number</span>
    <span class="contact-sep">•</span>
    <span class="contact-web">web site&nbsp; here</span>
  </footer>
</article>
</body>
</html>
```